High-end Oceanfront Real Estate Group Needs Clean, Modern Web Design

I’m looking for a clean, professional, modern and beautiful homepage web design for a Real Estate group in Southern California, USA.

The group/company is “Marlow on the Shore,” and they specialize in high end (i.e. expensive), oceanfront real estate in the Orange County area.

The look and feel of the page should accentuate the brand qualities: luxurious/expensive, professional, and beautiful (Orange County is one of the most beautiful areas in all the US and we would love the site to emphasize the beautiful beaches and scenery it has to offer).

Looks we like:
• www.brantleyhomesrealty.example
• www.keptbyfenwick.example -- I think the design is pretty out-dated in this site, but I like the organization/layout of the site

Header Tags (I don’t know if we can fit all of these, may need a side-menu, but I’d prefer header title only if possible):
• Welcome
• Featured Listings
• Previously Sold
• Sell
• Property Search
• Team
• Videos
• Blog
• Explore O.C.
• Contact

I have attached the beach and logo pics that we would like to use as the header, a few pictures of the team, and one sample home/view pic which can be used in any of the other sections (for pictures of the homes, just find expensive oceanfront houses and that will be fine).

I promise to provide feedback to each and every design submission. I appreciate the hard work that all of you are putting into your designs. There can be only one contest winner, but I hope to give all of you helpful feedback to submit the best designs possible!

Target Market(s)

Very wealthy home owners of oceanfront properties. These properties are worth several millions of dollars, and thus the site and brand needs to be targeted to very wealthy, successful individuals and families (both US and international buyers).

Industry/Entity Type

Real Estate

Number of Pages Required

2 page

Requirements
Must have
• I don’t want to give too many requirements, because I want to let you all be creative. However, here are the few Must Haves:
• Must submit 2 page designs (a home page and a sub page)
• Must use logo provided
• Focus is mostly on homes, but I would like to include some beach/ocean imagery as well
• The first “item” on the home page should be an accordion/slider which shows pictures of homes and with 1 line of text: “List with the Leader” and two link buttons: “Sell Your Home” and “Buy Your Home”
• Color palette needs to be mainly blues--to match ocean and sky blue
• Exported in all major formats (psd,ai,eps,png,jpeg,etc)
Nice to have
• We don’t necessarily need all of these, but would like to feature most:
• List of videos
• “Meet the Team”—brief team bios and pics
• Link(s) to Blog
• “List with the Leader” – section on why they should choose this firm
• Featured Listings
• Previously Sold

```html
<!DOCTYPE html>
<html lang="en">
<head>
<meta charset="utf-8">
<title>Marlow on the Shore</title>
<link rel="stylesheet" href="https://fonts.googleapis.com/css2?family=Open+Sans:wght@300;400;600;700&display=swap">
<style>
:root{
  --blue:#1b4fa3;
  --blue-btn:#1c4fb2;
  --navy:#1d3f89;
  --navy-line:#3b5ba0;
  --sky:#eaf1fb;
  --tab-off:#a8b8d5;
  --ink:#333;
  --muted:#777;
  --grey-head:#9a9a9a;
  --rule:#d9d9d9;
  --white:#fff;
}
*{margin:0;padding:0;box-sizing:border-box}
html,body{width:1200px;height:2903px;overflow:hidden}
body{font-family:"Open Sans",Arial,sans-serif;color:var(--ink);background:var(--white);position:relative}
.abs{position:absolute}
/* nav */
.top-nav{position:absolute;top:0;left:0;width:1200px;height:44px;display:flex;align-items:center;padding-left:100px;gap:0;font-size:13px;color:#555;text-transform:uppercase}
.top-nav a{color:inherit;text-decoration:none;margin-right:33px}
.top-nav a.active{color:#222;font-weight:600}
.top-nav svg{margin-left:2px}
/* hero */
.hero{position:absolute;top:43px;left:0;width:1200px;height:615px;background:linear-gradient(180deg,#3f86d6 0%,#8cc0ec 22%,#5d8fb5 28%,#3e6b3d 42%,#2f5a24 62%,#4d7c2e 80%,#6b5a44 100%)}
.brand-box{position:absolute;left:499px;top:21px;width:201px;height:143px;background:rgba(255,255,255,.55);display:flex;align-items:center;justify-content:center;text-align:center;font-weight:300;font-size:27px;line-height:1.15;color:var(--blue);letter-spacing:2px;text-transform:uppercase}
.hero-tag{position:absolute;left:445px;top:456px;width:304px;height:33px;background:rgba(240,240,240,.92);font-weight:700;font-size:23px;color:#222;text-align:center;line-height:33px}
.btn-solid{position:absolute;top:499px;height:39px;background:var(--blue-btn);color:var(--white);font-weight:600;font-size:17px;text-align:center;line-height:39px;text-transform:uppercase}
.slide-arrow{position:absolute;top:295px}
/* welcome */
.intro-title{position:absolute;top:702px;width:1200px;text-align:center;font-size:29px;color:var(--blue);font-weight:400}
.intro-copy{position:absolute;top:745px;left:230px;width:740px;text-align:center;font-size:12.5px;line-height:21px;color:#555}
.rule{position:absolute;top:838px;left:99px;width:1000px;height:1px;background:var(--rule)}
.sec-head{position:absolute;top:882px;font-size:27px;color:var(--blue);font-weight:400}
.video{position:absolute;width:213px;height:146px}
.video .play{position:absolute;left:50%;top:50%;width:30px;height:22px;margin:-11px 0 0 -15px;background:#d3101a;border-radius:5px}
.video .play::after{content:"";position:absolute;left:12px;top:6px;border-left:9px solid #fff;border-top:5px solid transparent;border-bottom:5px solid transparent}
.member{position:absolute;left:631px;width:470px;height:146px}
.member .photo{position:absolute;left:0;top:0;width:137px;height:146px}
.member .info{position:absolute;left:151px;top:-6px;width:320px}
.member h3{font-size:19px;font-weight:400;color:#222;margin-bottom:7px}
.member .contact{font-size:10.5px;line-height:18px;color:#333}
.member p{font-size:10.5px;line-height:16px;color:#888;margin-top:10px}
.member .more{font-size:10.5px;color:var(--blue);font-weight:600;margin-top:10px;display:block}
/* listings */
.band{position:absolute;left:0;width:1200px;background:var(--sky)}
.tab{position:absolute;top:40px;height:35px;color:var(--white);font-size:19px;font-weight:600;text-align:center;line-height:35px;text-transform:uppercase}
.tab.on{background:var(--blue-btn)}
.tab.on::after{content:"";position:absolute;left:50%;bottom:-8px;margin-left:-8px;border-left:8px solid transparent;border-right:8px solid transparent;border-top:8px solid var(--blue-btn)}
.tab.off{background:var(--tab-off)}
.card{position:absolute;width:213px;background:var(--white);box-shadow:0 2px 3px rgba(0,0,0,.08)}
.card .pic{height:178px}
.card .body{padding:14px 17px}
.card h4{font-size:13px;font-weight:600;color:#333}
.card .meta{font-size:10.5px;color:#888;line-height:16px;margin-top:6px}
.band-arrow{position:absolute}
/* leader */
.leader-title{position:absolute;top:1812px;width:1200px;text-align:center;font-size:25px;color:var(--grey-head);font-weight:400;text-transform:uppercase}
.leader-copy{position:absolute;top:1858px;left:240px;width:720px;text-align:center;font-size:12.5px;line-height:20px;color:#555}
.btn-line{position:absolute;top:1937px;height:40px;border:1px solid #555;color:var(--blue);font-size:17px;text-align:center;line-height:38px;text-transform:uppercase;background:var(--white)}
.btn-line.buy{color:#333}
/* blog */
.blog-title{position:absolute;top:56px;width:1200px;text-align:center;font-size:19px;color:var(--blue);font-weight:600}
.post .body{padding:16px 17px}
.post h4{font-size:13px;line-height:19px;font-weight:600;color:#333}
.post p{font-size:10.5px;line-height:15px;color:#888;margin-top:14px}
.post time{display:block;font-size:12px;color:#333;margin-top:16px}
/* footer */
.foot-info{position:absolute;top:2632px;left:0;width:1200px;height:131px}
.fcol{position:absolute;top:43px}
.fcol .label{font-size:12px;color:#333}
.fcol .value{font-size:19px;color:var(--blue);margin-top:8px}
.fdiv{position:absolute;top:38px;width:1px;height:62px;background:var(--rule)}
.social{display:flex;gap:8px;margin-top:12px}
.social span{width:27px;height:27px;background:var(--blue-btn);border-radius:3px}
.news{display:flex;margin-top:10px}
.news .field{width:182px;height:32px;border:1px solid #ccc;font-size:10px;color:#999;line-height:30px;padding-left:10px}
.news .go{width:70px;height:32px;background:#5b9ee8;color:#fff;font-size:11px;text-align:center;line-height:32px}
.foot-band{position:absolute;top:2763px;left:0;width:1200px;height:140px;background:var(--navy)}
.foot-nav{position:absolute;top:24px;width:1200px;display:flex;justify-content:center;gap:36px;font-size:12px;color:#fff;text-transform:uppercase}
.foot-rule{position:absolute;top:64px;left:143px;width:914px;height:1px;background:var(--navy-line)}
.copyright{position:absolute;top:89px;width:1200px;text-align:center;font-size:11.5px;color:#d7e0f2}
</style>
</head>
<body>

<nav class="top-nav">
  <a class="active">Welcome</a><a>Featured Listings</a><a>Previously Sold</a><a>Sell</a><a>Property Search</a><a>Team</a><a>Videos</a><a>Blog</a><a>Explore O.C.</a><a>Contact</a>
  <svg width="14" height="14" viewBox="0 0 14 14"><circle cx="5.5" cy="5.5" r="4.2" fill="none" stroke="#1c4fb2" stroke-width="2"/><line x1="8.6" y1="8.6" x2="13" y2="13" stroke="#1c4fb2" stroke-width="2.4"/></svg>
</nav>

<header class="hero" role="img" aria-label="Oceanfront resort with palm trees, lawns and pavilion overlooking the Pacific coast">
  <div class="brand-box">Marlow<br>on the<br>Shore</div>
  <svg class="slide-arrow" style="left:8px" width="12" height="20" viewBox="0 0 12 20"><polyline points="10,2 2,10 10,18" fill="none" stroke="#fff" stroke-width="2"/></svg>
  <svg class="slide-arrow" style="right:8px" width="12" height="20" viewBox="0 0 12 20"><polyline points="2,2 10,10 2,18" fill="none" stroke="#fff" stroke-width="2"/></svg>
  <div class="hero-tag">LIST WITH THE LEADER</div>
  <div class="btn-solid" style="left:418px;width:176px">Sell Your Home</div>
  <div class="btn-solid" style="left:604px;width:176px">Buy Your Home</div>
</header>

<h1 class="intro-title">WELCOME TO MARLOW ON THE SHORE</h1>
<p class="intro-copy">We at MarlowontheShore are privileged to help people from all over the world find their dream homes in Monarch Beach, Laguna Beach, Newport Coast, Dana Point, San Clemente and San Juan Capistrano. Whether you are buying or selling a property in Orange County, we want to help you in the most efficient, professional way possible.</p>
<div class="rule"></div>

<h2 class="sec-head" style="left:124px">Featured Videos</h2>
<div class="video" style="left:126px;top:940px;background:linear-gradient(135deg,#3a3a2a,#8a7a60)" role="img" aria-label="Video thumbnail: agent introduction"><span class="play"></span></div>
<div class="video" style="left:366px;top:940px;background:linear-gradient(135deg,#2a2622,#6a5e50)" role="img" aria-label="Video thumbnail: luxury kitchen tour"><span class="play"></span></div>
<div class="video" style="left:126px;top:1120px;background:linear-gradient(135deg,#7a3a32,#4a5a3a)" role="img" aria-label="Video thumbnail: hillside villa"><span class="play"></span></div>
<div class="video" style="left:366px;top:1120px;background:linear-gradient(135deg,#4e6a3a,#8a7a6a)" role="img" aria-label="Video thumbnail: aerial view of estate"><span class="play"></span></div>

<h2 class="sec-head" style="left:629px">Meet the Team</h2>
<div class="member" style="top:940px">
  <div class="photo" style="background:linear-gradient(180deg,#7b95b8,#d8c2a8)" role="img" aria-label="Portrait of Nora Whitcombe"></div>
  <div class="info">
    <h3>Nora Whitcombe</h3>
    <div class="contact">M : 555.201.4410 &nbsp;&nbsp;|&nbsp;&nbsp; T : 555.201.4422<br>E : nwhitcombe@shorehomes.example</div>
    <p>Phasellus nisl est, condimentum vitae faucibus in, sollicitudin vel metus. Nunc sit amet consequat risus. Curabitur ac elit leo, in eleifend dui tellus, in scelerisque elit porttitor et.</p>
    <span class="more">MORE</span>
  </div>
</div>
<div class="member" style="top:1120px">
  <div class="photo" style="background:linear-gradient(180deg,#5a6878,#8a8f98)" role="img" aria-label="Portrait of Glen"></div>
  <div class="info">
    <h3>Glen</h3>
    <div class="contact">M : 555.201.4410 &nbsp;&nbsp;|&nbsp;&nbsp; T : 555.201.4422<br>E : glen@shorehomes.example</div>
    <p>Phasellus nisl est, condimentum vitae faucibus in, sollicitudin vel metus. Nunc sit amet consequat risus. Curabitur ac elit leo, in eleifend dui tellus, in scelerisque elit porttitor et.</p>
    <span class="more">MORE</span>
  </div>
</div>

<section class="band" style="top:1316px;height:435px">
  <div class="tab on" style="left:387px;width:207px">Featured Listings</div>
  <div class="tab off" style="left:604px;width:189px">Previously Sold</div>
  <svg class="band-arrow" style="left:100px;top:237px" width="14" height="24" viewBox="0 0 14 24"><polyline points="12,2 2,12 12,22" fill="none" stroke="#999" stroke-width="2"/></svg>
  <svg class="band-arrow" style="left:1085px;top:237px" width="14" height="24" viewBox="0 0 14 24"><polyline points="2,2 12,12 2,22" fill="none" stroke="#999" stroke-width="2"/></svg>
  <div class="card" style="left:143px;top:112px"><div class="pic" style="background:linear-gradient(180deg,#2c4a8a,#8a8a90 60%,#4a4a48)" role="img" aria-label="Two-storey home at dusk"></div><div class="body"><h4>Aliquam erat volutpat</h4><div class="meta">12 Seacliff Row, Laguna Beach<br>$11,888,888</div></div></div>
  <div class="card" style="left:375px;top:112px"><div class="pic" style="background:linear-gradient(180deg,#3a6ec8,#c8a878 60%,#3a7a2a)" role="img" aria-label="Mediterranean house with lawn"></div><div class="body"><h4>Aliquam erat volutpat</h4><div class="meta">12 Seacliff Row, Laguna Beach<br>$11,888,888</div></div></div>
  <div class="card" style="left:607px;top:112px"><div class="pic" style="background:linear-gradient(180deg,#2a3a7a,#d8d8d8 55%,#6a6a6a)" role="img" aria-label="Modern white house with driveway"></div><div class="body"><h4>Aliquam erat volutpat</h4><div class="meta">12 Seacliff Row, Laguna Beach<br>$11,888,888</div></div></div>
  <div class="card" style="left:839px;top:112px"><div class="pic" style="background:linear-gradient(135deg,#3a2a1a,#b87a3a 60%,#d8b888)" role="img" aria-label="Living room with fireplace"></div><div class="body"><h4>Aliquam erat volutpat</h4><div class="meta">12 Seacliff Row, Laguna Beach<br>$11,888,888</div></div></div>
</section>

<h2 class="leader-title">List with the Leader</h2>
<p class="leader-copy">At MarlowontheShore, we are privileged to assist Clients with Purchasing, Selling, Leasing, and Property Care. We are honored to serve Clients from all over the world who have homes here in Orange County, and we not only handle their Real Estate needs, but we assist them in the care and oversight of their properties in their absence.</p>
<div class="btn-line" style="left:418px;width:178px">Sell Your Home</div>
<div class="btn-line buy" style="left:604px;width:178px">Buy Your Home</div>

<section class="band" style="top:2061px;height:571px">
  <h2 class="blog-title">BLOG</h2>
  <svg class="band-arrow" style="left:100px;top:238px" width="14" height="24" viewBox="0 0 14 24"><polyline points="12,2 2,12 12,22" fill="none" stroke="#999" stroke-width="2"/></svg>
  <svg class="band-arrow" style="left:1085px;top:238px" width="14" height="24" viewBox="0 0 14 24"><polyline points="2,2 12,12 2,22" fill="none" stroke="#999" stroke-width="2"/></svg>
  <article class="card post" style="left:143px;top:112px"><div class="pic" style="background:linear-gradient(180deg,#1a1040,#6a2a8a 55%,#d88a3a)" role="img" aria-label="City skyline at night"></div><div class="body"><h4>Integer eu massa lacinia, lacinia nulla non, volutpat purus.</h4><p>Fusce vitae lectus sit amet mi pulvinar maximus. Aenean placerat, nibh vel accumsan aliquet, magna nibh accumsan nibh, ac tempus nunc ipsum ac tellus.</p><time>Feb 27, 2015</time></div></article>
  <article class="card post" style="left:375px;top:112px"><div class="pic" style="background:linear-gradient(135deg,#e8f0b8,#7ab83a 60%,#2a8a2a)" role="img" aria-label="Green house shape held in hands"></div><div class="body"><h4>Integer eu massa lacinia, lacinia nulla non, volutpat purus.</h4><p>Fusce vitae lectus sit amet mi pulvinar maximus. Aenean placerat, nibh vel accumsan aliquet, magna nibh accumsan nibh, ac tempus nunc ipsum ac tellus.</p><time>Feb 27, 2015</time></div></article>
  <article class="card post" style="left:607px;top:112px"><div class="pic" style="background:linear-gradient(180deg,#5a8ac8,#8a6a4a 55%,#5a7a3a)" role="img" aria-label="Large timber and stone house"></div><div class="body"><h4>Integer eu massa lacinia, lacinia nulla non, volutpat purus.</h4><p>Fusce vitae lectus sit amet mi pulvinar maximus. Aenean placerat, nibh vel accumsan aliquet, magna nibh accumsan nibh, ac tempus nunc ipsum ac tellus.</p><time>Feb 27, 2015</time></div></article>
  <article class="card post" style="left:839px;top:112px"><div class="pic" style="background:linear-gradient(180deg,#9aa0a8,#c89a5a 55%,#2a6a9a)" role="img" aria-label="Modern home with pool at dusk"></div><div class="body"><h4>Integer eu massa lacinia, lacinia nulla non, volutpat purus.</h4><p>Fusce vitae lectus sit amet mi pulvinar maximus. Aenean placerat, nibh vel accumsan aliquet, magna nibh accumsan nibh, ac tempus nunc ipsum ac tellus.</p><time>Feb 27, 2015</time></div></article>
</section>

<footer>
  <div class="foot-info">
    <div class="fcol" style="left:101px"><div class="label">Address</div><div class="value">1870 Tidewater Lane, Laguna Beach, CA</div></div>
    <div class="fdiv" style="left:443px"></div>
    <div class="fcol" style="left:463px"><div class="label">Phone</div><div class="value">555.201.4410</div></div>
    <div class="fdiv" style="left:603px"></div>
    <div class="fcol" style="left:627px"><div class="label">Follow us on :</div>
      <div class="social"><span aria-label="Social link"></span><span aria-label="Social link"></span><span aria-label="Social link"></span><span aria-label="Social link"></span>
        <svg width="27" height="27" viewBox="0 0 27 27" aria-label="Email"><rect x="2" y="6" width="23" height="16" fill="none" stroke="#888" stroke-width="1.5"/><polyline points="2,6 13.5,15 25,6" fill="none" stroke="#888" stroke-width="1.5"/></svg>
      </div></div>
    <div class="fdiv" style="left:826px"></div>
    <div class="fcol" style="left:848px"><div class="label">Newsletter Subscribe</div>
      <div class="news"><div class="field">Email Address</div><div class="go">Subscribe</div></div></div>
  </div>
  <div class="foot-band">
    <div class="foot-nav"><span>Welcome</span><span>Featured Listings</span><span>Previously Sold</span><span>Sell</span><span>Property Search</span><span>Team</span><span>Videos</span><span>Blog</span><span>Explore O.C.</span><span>Contact</span></div>
    <div class="foot-rule"></div>
    <div class="copyright">Copyright &copy; 2015 &nbsp; Marlow on the Shore. &nbsp;All rights reserved.</div>
  </div>
</footer>

</body>
</html>
```